Business card - house cleaning company

We want friendly high end business card highlighting our services . NO LOGOs on back of card please.. no vertical cards NO DOUBLE BROOMS

2 owners of the company: Corinne Halvey & Joel Brandt

Included phone number: (555)318-2047

Email: brightlanetidy@mailnest.example

Website: www.brightlanetidy.example

Bonded & Insured

Alder Ridge, CO 80599

Slogan maybe: Bringing a brighter shine to every corner of home

We want elegant high end card for house cleaning service. Maybe 2 sided if needed. Can it have bullet points of some services we offer

Residential Home Cleaning
Vacation Rental Cleaning
Commercial Cleaning
Carpet Cleaning
Window Cleaning
Property Management
Property Inspections
Property Maintenance
Trash Removal
Concierge Services

Highlight service on back of card. If we can do a one sided card with all this that’s great as well. Not cartoony.

Our logo attached and a design somone I had Perrin but they put very little time in. Not Unique enough. If you can do a custom design with a feminine touch that be great.

You will be eliminated for not reading the brief. NO DOUBLE LOGOS NO DOUBLE BROOMS. PLEASE BE CREATIVE. IF POST SAME LOGO WITH SMAL CHANGES RHEY WILL BE ELIMINATED. BE CREATIVE.

Thank you everyone for your designs. please only use the logo 1 time. and would love to see some that dont look all the same. We appreciate your time.

Target Market(s)

Residential and vacation rental home cleaning maid service

Industry/Entity Type

House cleaning maid services

Contact Information for Business Card

For business card use logo. black and green one provided. others for example. I wil try find some example.. We want friendly high end look. 2 owners of the company: Corinne Halvey & Joel Brandt Included phone number: (555)318-2047 Email: brightlanetidy@mailnest.example Website: www.brightlanetidy.example Bonded & Insured Estes Park, CO Slogan maybe: Bringing a brighter shine to every corner of home or Quality Service Guaranteed We want elegant high end card for house cleaning service. Maybe 2 sided if needed. Can it have bullet points of some services we offer Residential Home Cleaning Vacation Rental Cleaning Commercial Cleaning Carpet Cleaning Window Cleaning Property Management Property Inspections Property Maintenance Trash Removal Concierge Services

Requirements
Must have
• For business card use logo . Creativity. black and green one provided. We want friendly high end look. 2 owners of the company: Corinne Halvey & Joel Brandt Included phone number: (555)318-2047 Email: brightlanetidy@mailnest.example Website: www.brightlanetidy.example Licensed Bonded & Insured Estes Park, CO Slogan maybe: Bringing a brighter shine to every corner of home or Quality Service Guaranteed We want elegant high end card for house cleaning service. Maybe 2 sided if needed. Can it have bullet points of some services we offer Residential Home Cleaning Vacation Rental Cleaning Commercial Cleaning Carpet Cleaning Window Cleaning Property Management Property Inspections Property Maintenance Trash Removal Concierge Services .. creatitivty a plus. whimsical. we like stars..
Nice to have
• we want much better than the example of biz card provided as example. logo has colors that are in our website palette as well. We are open to ideas for the business card design. Will pay tip to best work. PLEASE USE COMPLIMENTING COLORS. . WE LIKE BLACK AND WHITE, stars
Should not have
• NO DOUBLE LOGOS. READ READ. READ. YOU WILL BE ELIMINATED no double logos or double brooms same side of card. I want didfrent examples. please don't make all your submission look the same

```html
<!DOCTYPE html>
<html lang="en">
<head>
<meta charset="utf-8">
<title>Bright Lane Tidy Co. – Business Card</title>
<link href="https://fonts.googleapis.com/css2?family=Arimo:wght@400;700&display=swap" rel="stylesheet">
<style>
  :root {
    --green: #6f9a3e;
    --green-dark: #5f8734;
    --blue: #2a6690;
    --blue-deep: #235a80;
    --white: #ffffff;
    --paper: #e9ecef;
    --stage: #d5d9dd;
    --text-blue: #2a5f88;
  }
  * { margin: 0; padding: 0; box-sizing: border-box; }
  html, body { width: 1200px; height: 900px; overflow: hidden; }
  body {
    background: var(--stage);
    font-family: "Arimo", Arial, sans-serif;
    position: relative;
  }
  .card {
    position: absolute;
    width: 700px;
    height: 400px;
    border-radius: 24px;
    overflow: hidden;
    box-shadow: 0 10px 28px rgba(0,0,0,0.18);
  }

  /* Services side */
  .card-back { left: 60px; top: 40px; background: var(--green); color: var(--white); }
  .back-brand {
    position: absolute; left: 0; right: 0; top: 34px;
    text-align: center; font-weight: 700; font-size: 40px; letter-spacing: 0.5px;
  }
  .services-frame {
    position: absolute; left: 40px; top: 140px; width: 620px; height: 225px;
    border: 2px solid var(--white); border-radius: 18px;
  }
  .services-label {
    position: absolute; left: 50%; top: 124px; transform: translateX(-50%);
    background: var(--green); border: 2px solid var(--white); border-radius: 10px;
    padding: 5px 18px; font-weight: 700; font-size: 17px; letter-spacing: 1px;
  }
  .service-list {
    position: absolute; top: 172px; list-style: none;
    font-size: 17px; line-height: 1.7;
  }
  .service-list li::before, .service-list.right li::after {
    content: ""; display: inline-block; width: 7px; height: 7px;
    border-radius: 50%; background: var(--white); vertical-align: middle;
  }
  .service-list.left { left: 70px; }
  .service-list.left li::before { margin-right: 10px; }
  .service-list.right { right: 70px; text-align: right; }
  .service-list.right li::before { display: none; }
  .service-list.right li::after { margin-left: 10px; }

  /* Contact side */
  .card-front { left: 440px; top: 460px; background: var(--white); }
  .front-bands { position: absolute; inset: 0; }
  .front-decoration {
    position: absolute; left: 60px; top: 70px; width: 380px; height: 150px;
    border-radius: 50%;
    background: radial-gradient(ellipse at center, rgba(42,102,144,0.08), rgba(111,154,62,0.04) 55%, rgba(255,255,255,0) 75%);
  }
  .front-brand {
    position: absolute; right: 40px; top: 48px;
    font-weight: 700; font-size: 40px; color: var(--text-blue);
  }
  .person-name {
    position: absolute; left: 40px; top: 176px;
    font-weight: 700; font-size: 28px; color: var(--green);
  }
  .person-role {
    position: absolute; left: 40px; top: 212px;
    font-size: 18px; color: var(--text-blue);
  }
  .badge-text {
    position: absolute; right: 30px; top: 177px;
    font-size: 18px; color: var(--white);
  }
  .address {
    position: absolute; right: 30px; top: 232px;
    font-size: 19px; color: var(--white);
  }
  .contact-list {
    position: absolute; left: 36px; top: 262px; list-style: none;
    color: var(--white); font-size: 18px; line-height: 25px;
  }
  .contact-list li { display: flex; align-items: center; gap: 10px; }
  .contact-list svg { width: 16px; height: 16px; flex: none; }
  .slogan {
    position: absolute; left: 0; right: 0; top: 344px;
    text-align: center; font-size: 19px; color: var(--white); letter-spacing: 0.3px;
  }
</style>
</head>
<body>

<section class="card card-back" aria-label="Services side">
  <div class="back-brand">Bright Lane Tidy Co.</div>
  <div class="services-frame"></div>
  <div class="services-label">SERVICES WE OFFER</div>
  <ul class="service-list left">
    <li>Residential Home Cleaning</li>
    <li>Vacation Rental Cleaning</li>
    <li>Commercial Cleaning</li>
    <li>Carpet Cleaning</li>
    <li>Window Cleaning</li>
  </ul>
  <ul class="service-list right">
    <li>Property Management</li>
    <li>Property Inspections</li>
    <li>Property Maintenance</li>
    <li>Trash Removal</li>
    <li>Concierge Services</li>
  </ul>
</section>

<section class="card card-front" aria-label="Contact side">
  <svg class="front-bands" viewBox="0 0 700 400" width="700" height="400" aria-hidden="true">
    <polygon points="0,252 360,252 402,214 700,214 700,400 0,400" fill="var(--blue)"/>
    <polygon points="360,166 700,166 700,206 400,206" fill="var(--green)"/>
    <rect x="0" y="336" width="700" height="38" fill="var(--green)"/>
    <rect x="0" y="374" width="700" height="26" fill="var(--blue-deep)"/>
  </svg>
  <div class="front-decoration" role="img" aria-label="Faint mountain and sparkle watermark"></div>
  <div class="front-brand">Bright Lane Tidy Co.</div>
  <div class="person-name">Corinne Halvey</div>
  <div class="person-role">Owner</div>
  <div class="badge-text">Bonded &amp; Insured</div>
  <div class="address">Alder Ridge, CO 80599</div>
  <ul class="contact-list">
    <li>
      <svg viewBox="0 0 16 16" aria-hidden="true"><path d="M3 1.5l3 .5 1 3.2-1.6 1.3a9 9 0 0 0 4.1 4.1L10.8 9l3.2 1 .5 3-1.5 1.5C7 14.5 1.5 9 1.5 3z" fill="#fff"/></svg>
      (555)318-2047
    </li>
    <li>
      <svg viewBox="0 0 16 16" aria-hidden="true"><rect x="1" y="3" width="14" height="10" rx="1" fill="#fff"/><path d="M1.5 3.5L8 9l6.5-5.5" stroke="var(--blue)" stroke-width="1.4" fill="none"/></svg>
      brightlanetidy@mailnest.example
    </li>
    <li>
      <svg viewBox="0 0 16 16" aria-hidden="true"><circle cx="8" cy="8" r="6.5" fill="none" stroke="#fff" stroke-width="1.5"/><ellipse cx="8" cy="8" rx="2.6" ry="6.5" fill="none" stroke="#fff" stroke-width="1.2"/><line x1="1.5" y1="8" x2="14.5" y2="8" stroke="#fff" stroke-width="1.2"/></svg>
      www.brightlanetidy.example
    </li>
  </ul>
  <div class="slogan">Bringing a brighter shine to every corner of home</div>
</section>

</body>
</html>
```